Brantley Advisory Group provides support for renewable energy projects to utilities and suppliers

I need a professional looking business card that is both simple and elegant and unique. My clients are mostly large organizations not individuals. I am a consultant with my own company that is small but would like to give clients the impression I am larger. Smart grid, fiber optics, software, field hardware, distribution automation, substation automation, operations, energy storage/batteries, microgrids, customer service, strategy/roadmaps, conservation, Automated Metering Infrastruture (AMI or smart meters) are all areas of focus.

Target Market(s)

Utilities, suppliers, governmental agencies involved in energy. All types of energy especially natural gas and electrical. Especially renewable energy or green projects.

Contact Information for Business Card

Name - Mark Brantley Cell Phone - 425.318.2746 Email - mbrantley@brantleyag-example.com
Company - Brantley Advisory Group (logo) Title - Principal

Font styles to use
Serif
Sans Serif

Colors

Designer to choose colors to be used in the design.

Requirements
Must have
• Simple and professional and powerful.
• Unique/creative design.
Nice to have
• Utilize color scheme to accent logo colors. Maybe some geometric pattern on edge of card with color.
Should not have
• Busy, complicated, traditional

```html
<!DOCTYPE html>
<html lang="en">
<head>
<meta charset="utf-8">
<title>Brantley Advisory Group – Business Card</title>
<link href="https://fonts.googleapis.com/css2?family=Lato:wght@400;700&display=swap" rel="stylesheet">
<style>
  :root {
    --backdrop: #8c8c8c;
    --brand-blue: #1c3f96;
    --brand-green: #5b8b2f;
    --paper: #ffffff;
    --ink-light: #ffffff;
  }
  * { margin: 0; padding: 0; box-sizing: border-box; }
  html, body {
    width: 1200px;
    height: 960px;
    overflow: hidden;
  }
  body {
    background: var(--backdrop);
    font-family: "Lato", sans-serif;
    position: relative;
  }
  .card {
    position: absolute;
    left: 281px;
    width: 655px;
    height: 373px;
    border-radius: 28px;
    overflow: hidden;
  }
  .card--front { top: 59px; background: var(--paper); }
  .card--back { top: 506px; background: var(--brand-blue); }

  /* Front */
  .front__top {
    position: absolute;
    left: 0; top: 0;
    width: 100%;
    height: 221px;
  }
  .brand {
    position: absolute;
    display: flex;
    align-items: center;
    gap: 14px;
  }
  .brand--front { left: 56px; top: 116px; }
  .brand__mark {
    width: 36px;
    height: 36px;
    border: 4px solid var(--brand-green);
    border-radius: 4px;
  }
  .brand__name {
    font-weight: 700;
    font-size: 28px;
    color: var(--brand-blue);
    letter-spacing: 0.2px;
    white-space: nowrap;
  }
  .front__band {
    position: absolute;
    left: 0; top: 221px;
    width: 100%;
    height: 152px;
    background: var(--brand-blue);
    color: var(--ink-light);
  }
  .person {
    position: absolute;
    left: 67px;
    top: 26px;
  }
  .person__name {
    font-weight: 700;
    font-size: 28px;
    line-height: 1.1;
  }
  .person__title {
    font-weight: 400;
    font-size: 19px;
    margin-top: 6px;
  }
  .contact {
    position: absolute;
    left: 372px;
    top: 29px;
    list-style: none;
    font-size: 16px;
    line-height: 24px;
  }
  .contact__item {
    display: flex;
    align-items: center;
    gap: 8px;
    white-space: nowrap;
  }
  .contact__icon { width: 14px; height: 14px; flex: none; }

  /* Back */
  .brand--back {
    left: 50%;
    top: 168px;
    transform: translateX(-50%);
    gap: 18px;
  }
  .brand--back .brand__mark {
    width: 46px;
    height: 46px;
    border-color: var(--brand-green);
  }
  .brand--back .brand__name {
    color: var(--ink-light);
    font-size: 38px;
  }
  .back__url {
    position: absolute;
    left: 0; right: 0;
    top: 325px;
    text-align: center;
    color: var(--ink-light);
    font-size: 17px;
    letter-spacing: 1.8px;
  }
</style>
</head>
<body>

  <section class="card card--front" aria-label="Business card front">
    <div class="front__top">
      <div class="brand brand--front">
        <span class="brand__mark" aria-hidden="true"></span>
        <span class="brand__name">Brantley Advisory Group</span>
      </div>
    </div>
    <div class="front__band">
      <div class="person">
        <p class="person__name">Mark Brantley</p>
        <p class="person__title">Principal</p>
      </div>
      <ul class="contact">
        <li class="contact__item">
          <svg class="contact__icon" viewBox="0 0 16 16" aria-hidden="true">
            <path d="M4 2 L6.5 5 L5 7 Q6.5 10 9 11 L11 9.5 L14 12 L12.5 14 Q6 13.5 2 4 Z" fill="var(--brand-green)"/>
          </svg>
          425.318.2746
        </li>
        <li class="contact__item">
          <svg class="contact__icon" viewBox="0 0 16 16" aria-hidden="true">
            <rect x="1.5" y="4" width="13" height="9" fill="none" stroke="var(--brand-green)" stroke-width="1.5"/>
            <path d="M1.5 4 L8 9 L14.5 4" fill="none" stroke="var(--brand-green)" stroke-width="1.5"/>
          </svg>
          mbrantley@brantleyag-example.com
        </li>
        <li class="contact__item">
          <svg class="contact__icon" viewBox="0 0 16 16" aria-hidden="true">
            <circle cx="8" cy="8" r="6" fill="none" stroke="var(--brand-green)" stroke-width="1.3"/>
            <ellipse cx="8" cy="8" rx="2.6" ry="6" fill="none" stroke="var(--brand-green)" stroke-width="1.1"/>
            <path d="M2 8 H14 M3 5 H13 M3 11 H13" stroke="var(--brand-green)" stroke-width="1"/>
          </svg>
          www.brantleyag-example.com
        </li>
      </ul>
    </div>
  </section>

  <section class="card card--back" aria-label="Business card back">
    <div class="brand brand--back">
      <span class="brand__mark" aria-hidden="true"></span>
      <span class="brand__name">Brantley Advisory Group</span>
    </div>
    <p class="back__url">www.brantleyag-example.com</p>
  </section>

</body>
</html>
```